Packaging Design Project

Looking for a design for 2 chocolate box covers.
Dimensions: 7.5" x 7.5" x 1 .25"
5.75" x 5.75" x 1.25"
Desgn should be only 2 colors.

Visit our website to see our product:
www.lunabrookconfections.com
find us on facebook

Please see these guidelines for artwork on boxes:

Industry/Entity Type

Product

Requirements
Must have
• our logo as seen on our website

```html
<!DOCTYPE html>
<html lang="en">
<head>
<meta charset="utf-8">
<title>Lunabrook Confections – Box Cover</title>
<link rel="stylesheet" href="https://fonts.googleapis.com/css2?family=Cormorant+Garamond:wght@500&family=Montserrat:wght@500&family=Arimo&display=swap">
<style>
  :root {
    --ink: #000000;
    --ink-soft: #2b2b2b;
    --paper: #ffffff;
  }
  * { margin: 0; padding: 0; box-sizing: border-box; }
  html, body {
    width: 1200px;
    height: 1110px;
    overflow: hidden;
    background: var(--paper);
  }
  .canvas {
    position: relative;
    width: 1200px;
    height: 1110px;
    background: var(--paper);
  }
  .cover-pattern {
    position: absolute;
    left: 0;
    top: 0;
  }
  .label-frame {
    position: absolute;
    left: 283px;
    top: 235px;
    width: 650px;
    height: 613px;
    border: 3px solid var(--paper);
  }
  .label-frame-inner {
    position: absolute;
    left: 295px;
    top: 246px;
    width: 626px;
    height: 592px;
    border: 3px solid var(--paper);
  }
  .pattern-window {
    position: absolute;
    left: 314px;
    width: 588px;
    border: 3px solid var(--paper);
    background:
      repeating-linear-gradient(125deg, var(--ink) 0 46px, var(--ink-soft) 46px 90px, var(--ink) 90px 140px);
  }
  .pattern-window.top { top: 264px; height: 216px; }
  .pattern-window.bottom { top: 619px; height: 210px; }
  .name-band {
    position: absolute;
    left: 283px;
    top: 480px;
    width: 650px;
    height: 139px;
    background: var(--paper);
    text-align: center;
    color: var(--ink);
  }
  .brand-name {
    font-family: "Cormorant Garamond", serif;
    font-weight: 500;
    font-size: 47px;
    line-height: 1;
    margin-top: 46px;
    letter-spacing: 0.5px;
  }
  .tagline {
    font-family: "Montserrat", sans-serif;
    font-weight: 500;
    font-size: 14px;
    letter-spacing: 0.6px;
    margin-top: 12px;
  }
  .web-address {
    position: absolute;
    left: 314px;
    top: 802px;
    width: 588px;
    text-align: center;
    font-family: "Arimo", sans-serif;
    font-size: 17px;
    color: var(--paper);
  }
  .ingredients {
    position: absolute;
    left: 968px;
    top: 258px;
    height: 582px;
    width: 54px;
    writing-mode: vertical-rl;
    transform: rotate(180deg);
    font-family: "Arimo", sans-serif;
    font-size: 11.4px;
    line-height: 17px;
    color: var(--paper);
  }
</style>
</head>
<body>
<main class="canvas">
  <svg class="cover-pattern" width="1200" height="1110" viewBox="0 0 1200 1110" role="img" aria-label="Repeating pattern of white line-drawn cacao pods on black">
    <defs>
      <linearGradient id="pod-tone" x1="0" y1="0" x2="1" y2="1">
        <stop offset="0" stop-color="var(--ink)"/>
        <stop offset="0.5" stop-color="var(--ink-soft)"/>
        <stop offset="1" stop-color="var(--ink)"/>
      </linearGradient>
    </defs>
    <polygon points="180,114 1020,114 1044,138 1044,986 1020,1010 180,1010 156,986 156,138" fill="url(#pod-tone)"/>
  </svg>

  <div class="label-frame"></div>
  <div class="label-frame-inner"></div>

  <div class="pattern-window top" role="img" aria-label="Cacao pod pattern in white line art on black"></div>
  <div class="pattern-window bottom" role="img" aria-label="Cacao pod pattern in white line art on black"></div>

  <section class="name-band">
    <h1 class="brand-name">Lunabrook Confections</h1>
    <p class="tagline">HANDMADE IN THE VIENNESE STYLE</p>
  </section>

  <p class="web-address">www.lunabrookconfections.com</p>

  <p class="ingredients">Ingredients: Chocolate(sugar, chocolate liquor, milk, vanilla, soy lecithin)Sugar, corn syrup, Heavy cream, butter, inverted sugar, almonds, cashew, filbert, peanut, pecan,pistachio, walnut, coconut, raspberry, lime, lemon, coffee, ginger, strawberry, cranberry, cherry, orange, pectin, mint, green tea, maple syrup, salt, paprika, chili pepper.</p>
</main>
</body>
</html>
```